Bao Lotus Menu Design Project

This project is pretty straight forward. You will be given 3 files which include the following:
1. Our proposed menu
2. Our Company logo
3. A sample menu on what we are looking for design wise

Your job is to create a visually pleasing menu that is simple, clean and fresh. Please refer to our home website for additional information. (www.baolotus-example.com) Must be in eps or equivalent format.

Target Market(s)

20s to 40s

Industry/Entity Type

It Company

Requirements
Must have
• Company log
Must be in EPS format

```html
<!DOCTYPE html>
<html lang="en">
<head>
<meta charset="utf-8">
<title>Bao Lotus Menu</title>
<link href="https://fonts.googleapis.com/css2?family=PT+Sans:wght@400;700&family=Tinos:wght@700&display=swap" rel="stylesheet">
<style>
:root{
  --backdrop:#e9e4dc;
  --panel-dark:#1b1b1b;
  --panel-mid:#2b2b2b;
  --panel-grain:#333333;
  --text-light:#ffffff;
  --text-soft:#d9d9d9;
  --accent-red:#d1262a;
  --mark-red:#8e1f1f;
}
*{margin:0;padding:0;box-sizing:border-box}
html,body{width:1200px;height:572px;overflow:hidden;background:var(--backdrop)}
.canvas{position:relative;width:1200px;height:572px}
.menu-panel{
  position:absolute;top:84px;width:312px;height:398px;overflow:hidden;
  background:
    repeating-linear-gradient(90deg,rgba(255,255,255,.025) 0 2px,transparent 2px 9px,rgba(0,0,0,.12) 9px 11px,transparent 11px 17px),
    linear-gradient(180deg,var(--panel-mid),var(--panel-dark) 60%,var(--panel-grain));
  box-shadow:0 4px 12px rgba(0,0,0,.35);
  color:var(--text-light);
}
.panel-left{left:92px}
.panel-middle{left:440px}
.panel-right{left:788px}
.brand-mark{
  position:absolute;left:0;right:0;top:150px;text-align:center;
  font-family:"PT Sans",sans-serif;font-weight:700;font-size:64px;line-height:1;
  color:var(--mark-red);opacity:.22;
}
.section-title{
  position:absolute;width:200px;margin-left:-100px;text-align:center;
  font-family:"PT Sans",sans-serif;font-size:21px;font-weight:400;line-height:1;
}
.section-rule{position:absolute;height:2px;background:var(--accent-red)}
.dish{
  position:absolute;width:150px;margin-left:-75px;text-align:center;
  font-family:"Tinos",serif;font-weight:700;font-size:7.5px;line-height:9px;
}
.dish-desc{
  position:absolute;font-family:"PT Sans",sans-serif;font-size:6.5px;line-height:8.5px;
  color:var(--text-soft);
}
</style>
</head>
<body>
<main class="canvas">

  <section class="menu-panel panel-left">
    <div class="brand-mark">Bao<br>Lotus</div>
    <h2 class="section-title" style="left:155px;top:12px">Chicken</h2>
    <div class="section-rule" style="left:120px;top:34px;width:71px"></div>

    <div class="dish" style="left:58px;top:46px">General Tso's Chicken<br>$ 11.75</div>
    <p class="dish-desc" style="left:16px;top:66px;width:98px">Crispy dark meat chicken with chili peppers in a spicy tangerine sauce topped with scallions.</p>

    <div class="dish" style="left:244px;top:46px">Chicken Lettuce Cups<br>$ 11.75</div>
    <p class="dish-desc" style="left:190px;top:66px;width:110px">Minced white meat chicken with bell peppers, water chestnuts, black mushrooms, pine nuts, and white crunchies. Served with four lettuce cups.</p>

    <div class="dish" style="left:150px;top:108px">Moo Goo Gai Pan<br>$ 00</div>

    <div class="dish" style="left:65px;top:137px">Orange Chicken<br>$ 11.95</div>
    <p class="dish-desc" style="left:16px;top:157px;width:100px">Crispy chicken breast with onions and red and green bell peppers in a tangy orange Sauce.</p>

    <div class="dish" style="left:239px;top:137px">Kung Pao Chicken<br>$ 11.95</div>
    <p class="dish-desc" style="left:190px;top:157px;width:100px">Dark meat chicken with red bell peppers, peanuts and water chestnuts in picy red sauce.</p>

    <h2 class="section-title" style="left:156px;top:194px">Beef/Pork</h2>
    <div class="section-rule" style="left:112px;top:216px;width:88px"></div>

    <div class="dish" style="left:65px;top:231px">Mongolian Beef<br>$ 12.25</div>
    <p class="dish-desc" style="left:16px;top:251px;width:100px">Flank steak, garlic, ginger, and green onions on a bed of white crunchies.</p>

    <div class="dish" style="left:234px;top:231px">Pepper Steak<br>$ 11.95</div>
    <p class="dish-desc" style="left:190px;top:251px;width:100px">Flank steak, bell peppers onions and garlic in black pepper sauce.</p>

    <div class="dish" style="left:150px;top:288px">Sweet &amp; Sour Pork<br>$ 00</div>

    <div class="dish" style="left:60px;top:320px">Beef &amp; Broccoli<br>$ 11.95</div>
    <p class="dish-desc" style="left:16px;top:339px;width:100px">Flank steak, broccoli, and black mushrooms sautéed in a garlic brown sauce.</p>

    <div class="dish" style="left:237px;top:320px">Sliced BBQ Pork<br>$ 8.95</div>
    <p class="dish-desc" style="left:190px;top:339px;width:100px">Tender slices of juicy pork opped with scallions in a barbeque sauce.</p>
  </section>

  <section class="menu-panel panel-middle">
    <div class="brand-mark">Bao<br>Lotus</div>
    <h2 class="section-title" style="left:152px;top:26px">Seafood</h2>
    <div class="section-rule" style="left:116px;top:48px;width:75px"></div>

    <div class="dish" style="left:65px;top:60px">Shrimp w/ Snow Peas<br>$ 13.95</div>
    <p class="dish-desc" style="left:16px;top:79px;width:100px">Large shrimp with snow peas water chestnuts carrots and ginger in a white wine sauce.</p>

    <div class="dish" style="left:235px;top:60px">Fish w/ ginger soy<br>$ 15.95</div>
    <p class="dish-desc" style="left:193px;top:79px;width:100px">Whole white fish filet steamed with ginger and topped with green onions and cilantro.</p>

    <div class="dish" style="left:155px;top:109px">Scallops<br>w/ black bean sauce<br>$ 00</div>

    <div class="dish" style="left:78px;top:142px">Kung Pao 3 treasures<br>$ 13.95</div>
    <p class="dish-desc" style="left:16px;top:162px;width:112px">Large shrimp, beef, and chicken breast with scallions, peanuts water chestnuts and chili peppers. Prepared mandarin-Style.</p>

    <div class="dish" style="left:234px;top:142px">Honey Walnut Shrimp<br>$ 13.95</div>
    <p class="dish-desc" style="left:193px;top:162px;width:100px">Lightly crisped savory shrimp with honey-Glazed walnuts.</p>

    <h2 class="section-title" style="left:154px;top:207px">Vegetables</h2>
    <div class="section-rule" style="left:106px;top:231px;width:96px"></div>

    <div class="dish" style="left:66px;top:257px">Bak Choy w/ Mushrooms<br>$ 6.95</div>
    <p class="dish-desc" style="left:16px;top:277px;width:104px">Baby bokchoy and black mushrooms sautéed in a brown sauce.</p>

    <div class="dish" style="left:246px;top:257px">Spicy Garlic Eggplant<br>$ 8.95</div>
    <p class="dish-desc" style="left:210px;top:277px;width:96px">Sautéed chinese eggplant, red onions and scallions in a spicy garlic sauce.</p>

    <div class="dish" style="left:155px;top:294px">Spinach w/ garlic<br>$ 6.95</div>
    <p class="dish-desc" style="left:125px;top:314px;width:60px;text-align:center">Sautéed spinach with garlic.</p>

    <div class="dish" style="left:60px;top:324px">Schezuan String Bean<br>$ 8.95</div>
    <p class="dish-desc" style="left:16px;top:344px;width:96px">Blue lake green beans and garlic sautéed with pickled szechwan vegetables.</p>

    <div class="dish" style="left:242px;top:324px">Fragrant Vegetables<br>$ 8.95</div>
    <p class="dish-desc" style="left:193px;top:344px;width:104px">Mixed vegetables with white wine, curry, garlic, black bean kungpao, or vegetarian sauce.</p>
  </section>

  <section class="menu-panel panel-right">
    <div class="brand-mark">Bao<br>Lotus</div>
    <h2 class="section-title" style="left:151px;top:20px">Noodles</h2>
    <div class="section-rule" style="left:114px;top:42px;width:75px"></div>

    <div class="dish" style="left:68px;top:52px">Chow Mein<br>$ 12.95</div>
    <p class="dish-desc" style="left:19px;top:72px;width:100px">Crispy egg noodles or soft lo mein noodles with large vegetables and chicken, pork or vegetables. Beef or shrimp instead add $1.00.</p>

    <div class="dish" style="left:237px;top:52px">Lo Mein<br>$ 10.95</div>
    <p class="dish-desc" style="left:188px;top:72px;width:100px">Soft lo mein noodles with shredded vegetables and chicken, pork, or vegetables. Beef or shrimp instead add $1.00.</p>

    <div class="dish" style="left:154px;top:123px">Seafood Noodles<br>$ 00</div>

    <div class="dish" style="left:70px;top:153px">Singapore Noodles<br>$ 10.95</div>
    <p class="dish-desc" style="left:17px;top:173px;width:110px">Shrimp, barbeque pork, bean sprouts, onions, egg, and bell peppers with rice noodles in a curry sauce</p>

    <div class="dish" style="left:235px;top:153px">Pad Thai<br>$ 12.95</div>
    <p class="dish-desc" style="left:188px;top:173px;width:100px">Rice noodles with chicken shrimp eggs, onions, and scallions topped with peanuts and cilantro.</p>
  </section>

</main>
</body>
</html>
```